Cellar Guard Sealing
Business Cards
Project: Cellar Guard Sealing
Cellar Guard Sealing -
Creative Brief
Professional
Dorian Whitcombe
4826 Fernhill Glen Court #317 Gainesville, VA 20155
dwhitcombe@cellarguardsealing.example
www.cellarguardsealing.example
by line is : because it's not just any house...it's your home!
open to suggestions...be creative

```html
<!DOCTYPE html>
<html lang="en">
<head>
<meta charset="utf-8">
<title>Cellar Guard Sealing – Stationery</title>
<link href="https://fonts.googleapis.com/css2?family=Open+Sans:wght@400;600;700&display=swap" rel="stylesheet">
<style>
  :root{
    --backdrop:#a6a8ab;
    --frame:#c9cbcd;
    --paper:#ffffff;
    --brand-blue:#1e6fc0;
    --deep-blue:#0d4f9e;
    --light-blue:#4fa3e6;
    --brand-green:#5cae3c;
    --ink:#4a4a4a;
  }
  *{box-sizing:border-box;margin:0;padding:0}
  html,body{width:1200px;height:625px;overflow:hidden}
  body{background:var(--frame);font-family:"Open Sans",Arial,sans-serif;color:var(--ink);position:relative}
  .backdrop{position:absolute;left:8px;top:8px;width:1184px;height:609px;background:var(--backdrop)}
  .sheet{position:absolute;background:var(--paper);overflow:hidden;box-shadow:0 1px 2px rgba(0,0,0,.15)}
  .swoosh{position:absolute;left:0;bottom:0;width:100%;display:block}

  .brand{display:flex;align-items:center;gap:4px;position:absolute}
  .brand-dot{border-radius:50%;background:var(--brand-blue);flex:none}
  .brand-name{font-weight:700;color:var(--brand-blue);text-transform:uppercase;line-height:1.05;letter-spacing:.01em}
  .tagline{position:absolute;color:var(--brand-green);font-size:3px;white-space:nowrap}

  .contact{position:absolute;text-align:right;font-size:4px;line-height:1.6;color:var(--ink);white-space:nowrap}

  /* business card front */
  .card-front{left:36px;top:271px;width:139px;height:89px}
  .card-front .brand{left:50%;top:50%;transform:translate(-50%,-50%);flex-direction:column;gap:3px}
  .card-front .brand-dot{width:16px;height:16px}
  .card-front .brand-name{font-size:5px;text-align:center}

  /* business card back */
  .card-back{left:36px;top:374px;width:139px;height:89px}
  .card-back .brand{left:8px;top:22px}
  .card-back .brand-dot{width:8px;height:8px}
  .card-back .brand-name{font-size:5.5px;width:52px}
  .card-back .holder{position:absolute;left:80px;top:10px;font-size:4.5px;line-height:1.5;white-space:nowrap}
  .card-back .holder strong{color:var(--brand-blue);font-weight:600}
  .card-back .holder .role{font-size:3.5px;margin-bottom:3px}
  .card-back .holder .line{font-size:3.2px}
  .card-back .site{position:absolute;left:80px;top:48px;font-size:3.2px;line-height:1.5;white-space:nowrap}

  /* letterhead */
  .letterhead{left:235px;top:34px;width:394px;height:554px}
  .letterhead .brand{left:24px;top:26px}
  .letterhead .brand-dot{width:12px;height:12px}
  .letterhead .brand-name{font-size:8px;width:92px}
  .letterhead .tagline{left:24px;top:50px}
  .letterhead .contact{right:26px;top:22px}

  /* envelope back */
  .envelope-back{left:679px;top:79px;width:490px;height:245px}
  .envelope-back .flap{position:absolute;left:0;top:0;width:100%;height:245px;display:block}

  /* envelope front */
  .envelope-front{left:679px;top:341px;width:490px;height:247px}
  .envelope-front .brand{left:28px;top:34px}
  .envelope-front .brand-dot{width:12px;height:12px}
  .envelope-front .brand-name{font-size:8px;width:92px}
  .envelope-front .tagline{left:28px;top:58px}
  .envelope-front .contact{right:30px;top:28px}
</style>
</head>
<body>
<div class="backdrop"></div>

<section class="sheet card-front" aria-label="Business card front">
  <div class="brand"><span class="brand-dot"></span><span class="brand-name">Cellar Guard Sealing</span></div>
</section>

<section class="sheet card-back" aria-label="Business card back">
  <div class="brand"><span class="brand-dot"></span><span class="brand-name">Cellar Guard Sealing</span></div>
  <div class="holder">
    <strong>Dorian Whitcombe</strong>
    <div class="role">Owner</div>
    <div class="line">Office 571.555.0148</div>
    <div class="line">Mobile 571.555.0172</div>
    <div class="line">Fax 571.555.0149</div>
  </div>
  <div class="site">dwhitcombe@cellarguardsealing.example<br>www.cellarguardsealing.example</div>
  <svg class="swoosh" viewBox="0 0 139 24" height="24" preserveAspectRatio="none" aria-hidden="true">
    <defs><linearGradient id="cardBlue" x1="0" x2="1"><stop offset="0" stop-color="var(--deep-blue)"/><stop offset="1" stop-color="var(--light-blue)"/></linearGradient></defs>
    <path d="M0 4 Q60 14 139 10 L139 24 L0 24Z" fill="var(--brand-green)"/>
    <path d="M0 7 Q60 17 139 12 L139 24 L0 24Z" fill="url(#cardBlue)"/>
  </svg>
</section>

<section class="sheet letterhead" aria-label="Letterhead">
  <div class="brand"><span class="brand-dot"></span><span class="brand-name">Cellar Guard Sealing</span></div>
  <div class="tagline">because it's not just any house...it's your home!</div>
  <div class="contact">
    4826 Fernhill Glen Court #317 Gainesville, VA 20155<br>
    Phone 571.555.0148 Fax 571.555.0149<br>
    dwhitcombe@cellarguardsealing.example<br>
    <strong>www.cellarguardsealing.example</strong>
  </div>
  <svg class="swoosh" viewBox="0 0 394 80" height="80" preserveAspectRatio="none" aria-hidden="true">
    <defs><linearGradient id="sheetBlue" x1="0" x2="1"><stop offset="0" stop-color="var(--deep-blue)"/><stop offset=".6" stop-color="var(--brand-blue)"/><stop offset="1" stop-color="var(--light-blue)"/></linearGradient></defs>
    <path d="M0 6 Q150 44 394 58 L394 80 L0 80Z" fill="var(--brand-green)"/>
    <path d="M0 12 Q150 50 394 60 L394 80 L0 80Z" fill="url(#sheetBlue)"/>
  </svg>
</section>

<section class="sheet envelope-back" aria-label="Envelope back">
  <svg class="flap" viewBox="0 0 490 245" preserveAspectRatio="none" aria-hidden="true">
    <defs>
      <radialGradient id="flapGlow" cx=".45" cy=".2" r=".7"><stop offset="0" stop-color="var(--light-blue)"/><stop offset=".6" stop-color="var(--brand-blue)"/><stop offset="1" stop-color="var(--deep-blue)"/></radialGradient>
    </defs>
    <path d="M0 0 H490 V92 Q470 118 440 110 Q250 80 0 98Z" fill="url(#flapGlow)"/>
  </svg>
</section>

<section class="sheet envelope-front" aria-label="Envelope front">
  <div class="brand"><span class="brand-dot"></span><span class="brand-name">Cellar Guard Sealing</span></div>
  <div class="tagline">because it's not just any house...it's your home!</div>
  <div class="contact">
    4826 Fernhill Glen Court #317 Gainesville, VA 20155<br>
    Phone 571.555.0148 Fax 571.555.0149<br>
    dwhitcombe@cellarguardsealing.example<br>
    <strong>www.cellarguardsealing.example</strong>
  </div>
  <svg class="swoosh" viewBox="0 0 490 60" height="60" preserveAspectRatio="none" aria-hidden="true">
    <defs><linearGradient id="envBlue" x1="0" x2="1"><stop offset="0" stop-color="var(--deep-blue)"/><stop offset=".6" stop-color="var(--brand-blue)"/><stop offset="1" stop-color="var(--light-blue)"/></linearGradient></defs>
    <path d="M0 4 Q190 34 490 44 L490 60 L0 60Z" fill="var(--brand-green)"/>
    <path d="M0 10 Q190 40 490 46 L490 60 L0 60Z" fill="url(#envBlue)"/>
  </svg>
</section>
</body>
</html>
```